"Torvela" (spanish restaurant) "Bar de Tapas"

"Torvela" is a spanish restaurant located in the city of Santo Domingo, Dominican Republic. It needs a new and fresh idea for its business card. I would like to take the idea of one of the spaces of the restaurant represented on a business card, for example, the blue and emblematic entrance door of the restaurant, or maybe the bricks on the main room of the restaurant, or how about the bar. Any idea it's good! I invite all the creative designers to participate on the suggestions of it.

What doe sit need? It needs this information on it:

Name: Torvela
Business: Restaurante
Address: Calle Benito Sorel 00, Las Quintas
Phone number: 809-000-0000
website: www.torvelarestaurante.example

Reason: NEED MORE OPTION FOR IT. I WANT YOU TO EXPRESS YOUR DESIGN AS YOU WANT TO NOT AS I ASK YOU TO.

Industry/Entity Type

Restaurant

Contact Information for Business Card

c/Benito Sorel 47

Requirements
Must have
• Creativity. I'm open to new and fresh ideas.
Nice to have
• The entrance door (blue one) would be a plus in the design of the card. Maybe the background could be images of materials like bricks or wood, like the ones in the pictures of the restaurant.

```html
<!DOCTYPE html>
<html lang="es">
<head>
<meta charset="utf-8">
<title>Torvela — Tarjetas de presentación</title>
<link href="https://fonts.googleapis.com/css2?family=Tinos:wght@400;700&display=swap" rel="stylesheet">
<style>
  :root {
    --backdrop: #d9d9d9;
    --card: #000000;
    --ink: #ffffff;
    --gold: #8e7b4e;
    --ghost: #1c1c1c;
    --night: #0a0a0c;
    --stone: #5a4a35;
    --glow: #c9a36a;
  }
  * { margin: 0; padding: 0; box-sizing: border-box; }
  html, body { width: 1200px; height: 900px; overflow: hidden; }
  body {
    background: var(--backdrop);
    position: relative;
    font-family: "Tinos", "Times New Roman", serif;
    color: var(--ink);
  }
  .card {
    position: absolute;
    top: 79px;
    width: 428px;
    height: 730px;
    background: var(--card);
    overflow: hidden;
  }
  .card--front { left: 144px; }
  .card--back { left: 641px; }

  .ghost-mark {
    position: absolute;
    left: 0; right: 0;
    top: 250px;
    text-align: center;
    color: var(--ghost);
    line-height: 1;
    white-space: nowrap;
  }
  .ghost-mark__tag { font-size: 40px; letter-spacing: 2px; }
  .ghost-mark__name { font-size: 170px; font-weight: 700; letter-spacing: -2px; margin: 6px 0; margin-left: -40px; }
  .ghost-mark__sub { font-size: 52px; letter-spacing: 3px; }

  .lockup { position: absolute; left: 0; right: 0; text-align: center; line-height: 1; }
  .lockup__tag { letter-spacing: 0.5px; }
  .lockup__name { font-weight: 700; }
  .lockup__sub { letter-spacing: 1px; }

  .card--front .lockup { top: 285px; }
  .card--front .lockup__tag { font-size: 14px; }
  .card--front .lockup__name { font-size: 58px; margin: 6px 0 4px; }
  .card--front .lockup__sub { font-size: 16px; }

  .card--back .lockup { top: 56px; }
  .card--back .lockup__tag { font-size: 20px; color: var(--ink); }
  .card--back .lockup__name { font-size: 84px; color: var(--gold); margin: 8px 0 6px; }
  .card--back .lockup__sub { font-size: 26px; }

  .storefront-photo {
    position: absolute;
    left: 0; right: 0;
    top: 205px;
    height: 430px;
    background:
      radial-gradient(ellipse at 60% 70%, rgba(201,163,106,0.55), rgba(0,0,0,0) 55%),
      linear-gradient(180deg, var(--night) 0%, #1b1a17 35%, var(--stone) 70%, #111 100%);
  }

  .contact {
    position: absolute;
    left: 0; right: 0;
    text-align: center;
    font-size: 15px;
    line-height: 20px;
  }
  .card--front .contact { top: 682px; }
  .card--back .contact { top: 649px; }
</style>
</head>
<body>
  <section class="card card--front">
    <div class="ghost-mark" aria-hidden="true">
      <div class="ghost-mark__tag">BAR DE TAPAS</div>
      <div class="ghost-mark__name">TORVELA</div>
      <div class="ghost-mark__sub">RESTAURANTE</div>
    </div>
    <div class="lockup">
      <div class="lockup__tag">BAR DE TAPAS</div>
      <div class="lockup__name">TORVELA</div>
      <div class="lockup__sub">RESTAURANTE</div>
    </div>
    <p class="contact">www.torvelarestaurante.example</p>
  </section>

  <section class="card card--back">
    <div class="lockup">
      <div class="lockup__tag">BAR DE TAPAS</div>
      <div class="lockup__name">TORVELA</div>
      <div class="lockup__sub">RESTAURANTE</div>
    </div>
    <div class="storefront-photo" role="img" aria-label="Night photograph of the restaurant facade with palm trees, lit terrace and outdoor tables"></div>
    <p class="contact">
      C/ Benito Sorel no. 47, Las Quintas<br>
      Tel.: 809-000-0000<br>
      www.torvelarestaurante.example
    </p>
  </section>
</body>
</html>
```